4 sided DL flyer for a high end jewellery brand

I need a 4 sided DL flyer (21cm X 10cm) from my jewellery brand, ELUNE. My brand is UPSCALE and the flyer should be ELEGANT. I am uploading some sample images that can be used to create the flyer; however, I will get the final images in few days time. I am also attaching the following (1) My logo files - has the words ELUNE and icon (2) my business card - the front has the marble background that I am looking to use for the flyer and the logo style (gold foil). The back has the business details (3) mood board - blush pink/copper can also be used. Also please have space to write few lines about the brand and jewellery within the flyer. The flyer should be landscape.
Look and feel

```html
<!DOCTYPE html>
<html lang="en">
<head>
<meta charset="utf-8">
<title>ELUNE – Exquisite Silver Jewellery Flyer</title>
<link href="https://fonts.googleapis.com/css2?family=Josefin+Sans:wght@300;400;600&family=Montserrat:wght@400;500&display=swap" rel="stylesheet">
<style>
  :root{
    --blush:#e8918c;
    --blush-soft:#f2b5ae;
    --copper:#e9a064;
    --ink:#1d1d1f;
    --marble-light:#fbfbfb;
    --marble-mid:#eeeeee;
    --marble-edge:#e6e7e8;
    --rule:#8f8f8f;
    --flourish:#5a5a5a;
    --stage:#e9e9e9;
  }
  *{box-sizing:border-box;margin:0;padding:0}
  html,body{width:1200px;height:1200px;overflow:hidden;background:var(--stage)}
  body{position:relative;font-family:'Montserrat',sans-serif}

  .spread{position:absolute;left:50px;top:325px;width:1100px;height:550px;display:flex;
    box-shadow:0 10px 30px rgba(0,0,0,.18)}
  .panel{position:relative;width:550px;height:550px;overflow:hidden}

  /* back panel */
  .panel--back{background:var(--blush)}
  .beads-photo{position:absolute;left:0;top:0;width:230px;height:230px;
    background:radial-gradient(circle at 40% 45%,var(--copper) 0%,#f0b9a8 45%,var(--blush-soft) 70%,var(--blush) 100%)}
  .sparkle{position:absolute;left:0;bottom:0;width:550px;height:220px;
    background:linear-gradient(180deg,rgba(232,145,140,0) 0%,rgba(240,180,172,.55) 100%)}
  .model-photo{position:absolute;right:30px;bottom:0;width:250px;height:330px;
    background:linear-gradient(180deg,#e7b79b 0%,#d9a08a 30%,#2a2c3a 45%,#23252f 100%);
    border-radius:110px 110px 0 0}
  .brand-copy{position:absolute;left:295px;top:40px;width:230px;font-size:11px;line-height:1.45;color:var(--ink)}
  .contact{position:absolute;left:40px;bottom:40px;color:var(--ink)}
  .brand-name{font-family:'Josefin Sans',sans-serif;font-weight:400;letter-spacing:.28em;font-size:20px;color:var(--ink);margin-bottom:12px}
  .contact-list{list-style:none;font-size:14px;line-height:1.4}
  .contact-list li{display:flex;align-items:flex-start;gap:7px}
  .contact-list svg{flex:none;margin-top:4px}

  /* front panel */
  .marble-texture{position:absolute;inset:0;
    background:radial-gradient(ellipse at 50% 42%,var(--marble-light) 0%,var(--marble-mid) 70%,var(--marble-edge) 100%)}
  .front-name{position:absolute;top:60px;width:100%;text-align:center;
    font-family:'Josefin Sans',sans-serif;font-weight:400;font-size:34px;letter-spacing:.35em;color:var(--blush);padding-left:.35em}
  .rings-photo{position:absolute;left:125px;top:140px;width:300px;height:150px;
    background:linear-gradient(90deg,#dcdcdc 0%,#f2f2f2 35%,#e0c079 60%,#c9a25a 100%);border-radius:75px}

  .ornament-row{position:absolute;left:70px;width:410px;height:28px;display:flex;align-items:center;gap:10px}
  .ornament-row--top{top:326px}
  .ornament-row--bottom{top:420px}
  .ornament-rule{flex:1;height:1px;background:var(--rule)}
  .flourish{flex:none;width:190px;height:24px;border-radius:12px;
    background:linear-gradient(90deg,rgba(90,90,90,.15) 0%,rgba(90,90,90,.55) 50%,rgba(90,90,90,.15) 100%)}
  .ornament-row--top .ornament-rule:first-child{flex:1.6}

  .headline{position:absolute;left:0;top:370px;width:100%;text-align:center;
    font-family:'Josefin Sans',sans-serif;font-weight:600;font-size:27px;letter-spacing:.03em;color:var(--blush)}
</style>
</head>
<body>
  <main class="spread">
    <section class="panel panel--back">
      <div class="beads-photo" role="img" aria-label="Brushed copper and blush pink bead necklace"></div>
      <div class="sparkle"></div>
      <p class="brand-copy">Lorem Ipsum is simply dummy text of the printing and typesetting industry. Lorem Ipsum has been the industry's standard dummy text ever since the 1500s, when an unknown printer took a galley of type and scrambled it to make a type specimen book.</p>
      <div class="model-photo" role="img" aria-label="Woman in a navy top wearing a statement ring and watch"></div>
      <div class="contact">
        <div class="brand-name">ELUNE</div>
        <ul class="contact-list">
          <li><svg width="10" height="10" viewBox="0 0 10 10"><path d="M2 1l2 2-1 1a6 6 0 003 3l1-1 2 2-1.5 1.5C4 9 1 6 .5 2.5z" fill="currentColor"/></svg>61 4 5172 0986</li>
          <li><svg width="10" height="10" viewBox="0 0 10 10"><circle cx="5" cy="5" r="4" fill="none" stroke="currentColor"/><path d="M1 5h8M5 1v8" stroke="currentColor"/></svg>www.elune.com.au</li>
          <li><svg width="10" height="10" viewBox="0 0 10 10"><rect x=".5" y="2" width="9" height="6" fill="none" stroke="currentColor"/><path d="M.5 2l4.5 3 4.5-3" fill="none" stroke="currentColor"/></svg>info@elune.com.au</li>
          <li><svg width="10" height="10" viewBox="0 0 10 10"><path d="M5 10S1.5 6 1.5 3.5a3.5 3.5 0 017 0C8.5 6 5 10 5 10z" fill="currentColor"/></svg>PO Box 412, Linfield,<br>NSW 2090, Australia</li>
        </ul>
      </div>
    </section>

    <section class="panel panel--front">
      <div class="marble-texture" role="img" aria-label="White marble background with soft grey veining"></div>
      <div class="front-name">ELUNE</div>
      <div class="rings-photo" role="img" aria-label="Textured silver and gold rings set with small diamonds"></div>
      <div class="ornament-row ornament-row--top">
        <span class="ornament-rule"></span>
        <span class="flourish" role="img" aria-label="Ornamental scroll flourish"></span>
        <span class="ornament-rule"></span>
      </div>
      <h1 class="headline">EXQUISITE SILVER JEWELLERY</h1>
      <div class="ornament-row ornament-row--bottom">
        <span class="ornament-rule"></span>
        <span class="flourish" role="img" aria-label="Ornamental scroll flourish"></span>
        <span class="ornament-rule"></span>
      </div>
    </section>
  </main>
</body>
</html>
```